Package for a Mouthfreshener called VORA!!

We are looking for an awesome packaging design for a bran new product called “Vora Mouthfreshener”

This product is going to be made in USA so is really importar that ‘Made in USA” is part of the packaging.

We also need to include the ingredients that are going to be the following:
Saffron
cardamom
menthol
catechu
permited spices and falvors
tree nuts.

We are looking to haver this in a green or purple color and to clarify that the “best before” is for 2 years after the production date

Target Market(s)

Indian stores in usa

Colors
0094D4
00A9DD
6FCCEA
C7EBF8
E9F6FB
00AB8E
00BBA5
67D7C9
C6EFE9
E9F9F6
6B429C
8869AF
B7A5CE
E3DAEB
F3F0F8

Requirements
Must have
• Ingredients
Nice to have
• A good font and is important to mention is made in USA on images I upload an idea for the font

```html
<!DOCTYPE html>
<html lang="en">
<head>
<meta charset="utf-8">
<title>Vora Mouthfreshener – Box Dieline</title>
<link href="https://fonts.googleapis.com/css2?family=Roboto+Condensed:wght@700&display=swap" rel="stylesheet">
<style>
  :root {
    --paper: #ffffff;
    --purple-deep: #52286b;
    --purple-mid: #6b3d96;
    --purple-soft: #6a4390;
    --fold-line: #e0245e;
    --ink-light: #ffffff;
    --badge-ink: #6b429c;
  }
  html, body {
    margin: 0;
    padding: 0;
    width: 1200px;
    height: 849px;
    overflow: hidden;
    background: var(--paper);
  }
  .dieline {
    position: relative;
    width: 1200px;
    height: 849px;
    font-family: "Roboto Condensed", "Arial Narrow", sans-serif;
    font-weight: 700;
    color: var(--ink-light);
  }
  .panel { position: absolute; }
  .flap { background: var(--purple-mid); }
  .flap-top { left: 176.5px; top: 48.6px; width: 307.8px; height: 128.4px; }
  .flap-bottom { left: 176.5px; top: 690px; width: 307.8px; height: 129px; }
  .body-band {
    left: 47.2px; top: 177px; width: 873.5px; height: 513px;
    background: radial-gradient(ellipse at 30% 30%, var(--purple-soft) 0%, var(--purple-deep) 55%),
                var(--purple-deep);
    border-right: 1px solid var(--fold-line);
    box-sizing: border-box;
  }
  .fold {
    position: absolute;
    top: 177px;
    width: 1px;
    height: 513px;
    background: var(--fold-line);
  }
  .fold-a { left: 176.5px; }
  .fold-b { left: 484.3px; }
  .fold-c { left: 612.9px; }
  .sachet {
    left: 960px; top: 283px; width: 205.5px; height: 269px;
    background: radial-gradient(ellipse at 40% 30%, var(--purple-soft) 0%, var(--purple-deep) 60%);
  }
  .brand-name {
    position: absolute;
    font-weight: 700;
    color: var(--ink-light);
    text-align: center;
    line-height: 1;
    margin: 0;
  }
  .tagline {
    position: absolute;
    font-weight: 700;
    text-transform: uppercase;
    letter-spacing: 0.5px;
    color: var(--ink-light);
    text-align: center;
    margin: 0;
    white-space: nowrap;
    line-height: 1;
  }
  .flap-top .brand-name { left: 0; width: 100%; top: 22px; font-size: 48px; }
  .flap-top .tagline { left: 0; width: 100%; top: 89px; font-size: 18px; }
  .front-name { left: 176.5px; width: 307.8px; top: 300px; font-size: 120px; }
  .front-tagline { left: 176.5px; width: 307.8px; top: 467px; font-size: 18px; }
  .pack-badge {
    position: absolute;
    left: 268px; top: 594px; width: 123px; height: 40px;
    background: var(--ink-light);
    display: flex; align-items: center; justify-content: center; gap: 3px;
    color: var(--badge-ink);
    clip-path: polygon(0 10%, 95% 0, 100% 30%, 97% 55%, 100% 90%, 4% 100%, 0 70%, 3% 40%);
  }
  .pack-count { font-size: 28px; line-height: 1; }
  .pack-label { font-size: 11px; line-height: 1; text-transform: uppercase; }
  .origin {
    position: absolute;
    left: 176.5px; width: 307.8px; top: 648px;
    text-align: center; font-size: 17px; margin: 0;
  }
  .side-name { left: 637px; top: 205px; font-size: 72px; text-align: left; }
  .ingredients {
    position: absolute;
    left: 637px; top: 366px;
    font-size: 19px; line-height: 24px;
    margin: 0;
  }
  .ingredients h2 { font-size: 19px; margin: 0 0 24px; font-weight: 700; }
  .ingredients ul { list-style: none; margin: 0; padding: 0; }
  .sachet .brand-name { left: 0; width: 100%; top: 82px; font-size: 76px; }
  .sachet .tagline { left: 0; width: 100%; top: 180px; font-size: 11px; }
</style>
</head>
<body>
<main class="dieline">
  <section class="panel flap flap-top">
    <p class="brand-name">Vora</p>
    <p class="tagline">Fresh breath, bold flavor</p>
  </section>

  <section class="panel body-band" role="img" aria-label="Flowing purple marbled swirl background"></section>

  <div class="fold fold-a"></div>
  <div class="fold fold-b"></div>
  <div class="fold fold-c"></div>

  <p class="brand-name front-name">Vora</p>
  <p class="tagline front-tagline">Fresh breath, bold flavor</p>
  <div class="pack-badge">
    <span class="pack-count">50</span>
    <span class="pack-label">Packs<br>Inside</span>
  </div>
  <p class="origin">Made in USA</p>

  <p class="brand-name side-name">Vora</p>
  <div class="ingredients">
    <h2>Ingredients:</h2>
    <ul>
      <li>Saffron</li>
      <li>cardamom</li>
      <li>menthol</li>
      <li>catechu</li>
      <li>permited spices and falvors</li>
      <li>tree nuts.</li>
    </ul>
  </div>

  <section class="panel flap flap-bottom"></section>

  <section class="panel sachet" role="img" aria-label="Sachet front with purple marbled swirl background">
    <p class="brand-name">Vora</p>
    <p class="tagline">Fresh breath, bold flavor</p>
  </section>
</main>
</body>
</html>
```